Birchwood Forage Business Cards

I need a business card with my logo, number, Facebook account, and some information about what I am selling. Green card with logo on the front. 847-302-1596 phone number, @birchwoodforage Facebook, •Orchardgrass Hay •Alfalfa Hay •Mixed Grass Hay , and “Premium Quality Hay” all written on the back.

Target Market(s)

Hay

Contact Information for Business Card

Phone number, Facebook, different types of hay.

Colors
00AB8E
00BBA5
67D7C9
C6EFE9
E9F9F6

```html
<!DOCTYPE html>
<html lang="en">
<head>
<meta charset="utf-8">
<title>Birchwood Forage Business Cards</title>
<link href="https://fonts.googleapis.com/css2?family=Arimo:wght@400;700&family=Kaushan+Script&display=swap" rel="stylesheet">
<style>
  :root {
    --bg: #d2d2d2;
    --card-dark: #1f1f1f;
    --card-green: #00a859;
    --accent: #00b05c;
    --accent-light: #18f08a;
    --emboss-dark: #008c47;
    --white: #ffffff;
    --divider: #5a5a5a;
  }
  * { margin: 0; padding: 0; box-sizing: border-box; }
  html, body {
    width: 1200px; height: 800px; overflow: hidden;
    background: var(--bg);
    font-family: "Arimo", Arial, sans-serif;
  }
  .canvas { position: relative; width: 1200px; height: 800px; }
  .card {
    position: absolute; top: 245px;
    width: 540px; height: 310px;
    overflow: hidden;
  }

  /* Back card */
  .card-back { left: 40px; background: var(--card-dark); border-bottom: 3px solid var(--accent); }
  .brand-mark {
    position: absolute; left: 40px; top: 100px;
    display: flex; align-items: center; gap: 8px;
    color: var(--accent); font-weight: 700; font-size: 13px;
    white-space: nowrap;
  }
  .brand-mark .dot { width: 14px; height: 14px; border-radius: 50%; background: var(--accent); }
  .title-divider {
    position: absolute; left: 200px; top: 84px;
    width: 1px; height: 50px; background: var(--divider);
  }
  .card-title {
    position: absolute; left: 218px; top: 84px;
    font-family: "Kaushan Script", cursive;
    font-weight: 400;
    color: var(--white); font-size: 34px; line-height: 1.2;
    white-space: nowrap;
  }
  .contact-row {
    position: absolute; top: 178px;
    display: flex; align-items: center; gap: 8px;
    color: var(--white); font-size: 15px;
    white-space: nowrap;
  }
  .contact-phone { left: 58px; }
  .contact-social { left: 250px; }
  .icon-circle {
    width: 26px; height: 26px; border-radius: 50%;
    background: var(--accent);
    display: flex; align-items: center; justify-content: center;
  }
  .rule {
    position: absolute; left: 90px; right: 26px; top: 222px;
    height: 1px; background: var(--accent);
  }
  .product-list {
    position: absolute; left: 100px; top: 238px;
    list-style: none;
    display: grid; grid-template-columns: 160px 170px; row-gap: 10px;
    color: var(--white); font-size: 15px;
  }
  .product-list li { display: flex; align-items: center; gap: 7px; white-space: nowrap; }
  .product-list li::before {
    content: ""; width: 8px; height: 8px; border-radius: 50%; background: var(--accent);
  }

  /* Front card */
  .card-front { left: 620px; background: var(--card-green); }
  .front-mark {
    position: absolute; left: 36px; top: 150px;
    display: flex; align-items: center; gap: 8px;
    color: var(--accent-light); font-weight: 700; font-size: 17px;
    white-space: nowrap;
  }
  .front-mark .dot { width: 18px; height: 18px; border-radius: 50%; background: var(--accent-light); }
  .front-name {
    position: absolute; left: 240px; top: 98px;
    font-family: "Kaushan Script", cursive;
    font-size: 34px; line-height: 1.2; color: var(--emboss-dark);
    text-shadow: 1px 1px 0 rgba(255,255,255,0.18);
    white-space: nowrap;
  }
  .front-phone {
    position: absolute; left: 242px; top: 150px;
    font-weight: 700; font-size: 36px; letter-spacing: 1px;
    color: var(--emboss-dark);
    text-shadow: 1px 1px 0 rgba(255,255,255,0.18);
    white-space: nowrap;
  }
</style>
</head>
<body>
<main class="canvas">

  <section class="card card-back" aria-label="Business card back">
    <div class="brand-mark"><span class="dot"></span>Birchwood Forage</div>
    <div class="title-divider"></div>
    <h1 class="card-title">Birchwood Forage</h1>

    <div class="contact-row contact-phone">
      <span class="icon-circle">
        <svg width="14" height="14" viewBox="0 0 24 24" aria-hidden="true">
          <path fill="#1f1f1f" d="M6.6 10.8a15.1 15.1 0 0 0 6.6 6.6l2.2-2.2a1 1 0 0 1 1-.25 11.4 11.4 0 0 0 3.6.57 1 1 0 0 1 1 1V20a1 1 0 0 1-1 1A17 17 0 0 1 3 4a1 1 0 0 1 1-1h3.5a1 1 0 0 1 1 1c0 1.250.2 2.450.57 3.57a1 1 0 0 1-.25 1z"/>
        </svg>
      </span>
      847-302-1596
    </div>
    <div class="contact-row contact-social">
      <span class="icon-circle"></span>
      @birchwoodforage
    </div>

    <div class="rule"></div>

    <ul class="product-list">
      <li>Orchardgrass Hay</li>
      <li>Alfalfa Hay</li>
      <li>Mixed Grass Hay</li>
      <li>Premium Quality Hay</li>
    </ul>
  </section>

  <section class="card card-front" aria-label="Business card front">
    <div class="front-mark"><span class="dot"></span>Birchwood Forage</div>
    <p class="front-name">Birchwood Forage</p>
    <p class="front-phone">847-302-1596</p>
  </section>

</main>
</body>
</html>
```